International Manufacturing Business Needs A Heavy Hitting Wordpress Design!

We need wordpress template designs for a new website for our UK based International company Halvenmoor Fabrication Ltd. We manufacture and supply steel security doors and window units. We would like designs that feature the black and yellow industrial "stripes" that can be seen at our current site www.pelbrogates.com. The final design should communicate strength, power and weight to represent the quality of the products and the security that they provide.

It feels like we need 3 different types of page to be able to be created as per the current website at www.pelbrostrongdoors.com.

Homepage
Products/Accessories
Leadtimes/Downloads/Contact

It may be that 3 different page types can be created with one template. I'm totally open to this.

I don't like the way that the site currently handles product images, nobody wants to click on even thumbnail to see the product. http://pelbrostrongdoors.com/products/personnel-doors/

Totally open to suggestions on layout to enable the feeling outlined in the brief above.

Please ask if anything is not clear or you need answers to drill down on specifics.

Target Market(s)

Businesses that buy steel doors

Font styles to use
Sans Serif
Other font styles liked:
• Copperplate Gothic Bold - For Company Name but we are open to suggestions

Colors

Designer to choose colors to be used in the design.

Requirements
Must have
• Professional looking, clean design
• Conveys strength, power and weight to represent the quality of the products, the characteristics of steel and the security that they provide.
• Incorporates black and yellow stripes of our branding
• Ability to create pages with content as seen at www.pelbrostrongdoors.com
• A better way of showing the product images
Nice to have
• If possible. a design that gives off the feeling that not only do we supply the products we also make them in house too. I don't know what this looks like but a way of differentiating between a supply only business and one that manufacturers the product too.
Should not have
• We don't like the current thumbnail method of showing the product images

```html
<!DOCTYPE html>
<html lang="en">
<head>
<meta charset="utf-8">
<title>Halvenmoor Fabrication Ltd – Steel Security Doors</title>
<link href="https://fonts.googleapis.com/css2?family=Montserrat:wght@400;600;700;800&family=Open+Sans:wght@400;600&display=swap" rel="stylesheet">
<style>
:root{
  --green:#5fb585;
  --teal:#4d9a98;
  --yellow:#f2f20a;
  --ink:#1b1b1b;
  --black:#1d1d1d;
  --olive:#2c2f1f;
  --grey-bg:#f2f2f2;
  --line:#dcdcdc;
  --white:#ffffff;
  --muted:#555;
}
*{margin:0;padding:0;box-sizing:border-box}
html,body{width:1200px;height:3015px;overflow:hidden;background:var(--white)}
body{position:relative;font-family:"Open Sans",Arial,sans-serif;color:var(--ink)}
.abs{position:absolute}
h1,h2,h3,.brand,.nav a,.btn{font-family:"Montserrat",Arial,sans-serif}

/* Header */
.site-header{position:absolute;left:0;top:0;width:1200px;height:155px;background:var(--white);z-index:3}
.brand-mark{left:138px;top:30px;width:70px;height:70px;background:var(--green)}
.brand{left:236px;top:28px;font-weight:800;font-size:25px;line-height:30px;color:var(--ink);text-transform:uppercase}
.brand span{display:block;font-size:16px;font-weight:800;line-height:24px}
.call{left:812px;top:36px;display:flex;align-items:center;gap:18px}
.call-icon{width:32px;height:32px;border-radius:50%;background:var(--green);display:flex;align-items:center;justify-content:center}
.call small{display:block;font-family:"Montserrat",sans-serif;font-weight:700;font-size:10px;color:var(--ink)}
.call strong{display:block;font-family:"Montserrat",sans-serif;font-weight:700;font-size:20px;color:var(--green)}
.header-rule{left:236px;top:104px;width:834px;height:3px;background:var(--line)}
.header-rule::before{content:"";position:absolute;left:0;top:0;width:40px;height:3px;background:var(--green)}
.nav{left:236px;top:124px;width:834px;display:flex;justify-content:space-between}
.nav a{font-size:10.5px;font-weight:600;color:var(--ink);text-decoration:none;text-transform:uppercase}
.nav a.active{color:var(--green)}

/* Hero */
.hero{left:0;top:155px;width:1200px;height:528px;background:linear-gradient(90deg,#3a2c22 0%,#6b4a32 30%,#4a3324 55%,#8a8580 63%,#3a2a20 70%,#8c4a32 85%,#7a3f2c 100%)}
.hero h1{position:absolute;left:268px;top:222px;font-size:50px;font-weight:800;line-height:52px;color:var(--white)}
.hero h1 em{font-style:normal;color:var(--green);display:block}
.btn{display:inline-block;font-weight:700;font-size:12px;text-transform:uppercase;text-decoration:none;text-align:center}
.btn-teal{position:absolute;left:272px;top:400px;width:132px;height:38px;line-height:38px;background:var(--teal);color:var(--white)}
.dots{display:flex;gap:14px}
.dots i{width:10px;height:10px;border-radius:50%;background:var(--white);display:block}
.dots i.on{background:var(--teal)}
.hero .dots{position:absolute;left:542px;top:470px}

/* What we do */
.about{left:0;top:683px;width:1200px;height:635px;background:var(--olive);overflow:hidden}
.about svg{position:absolute;left:0;top:0}
.about h2{position:absolute;left:172px;top:70px;font-size:20px;font-weight:800;color:var(--white)}
.about .rule{position:absolute;left:174px;top:106px;width:64px;height:3px;background:var(--white)}
.about-text{position:absolute;left:172px;top:146px;width:340px;color:#e4e4e4;font-size:12px;line-height:16px}
.about-text p{margin-bottom:16px}
.btn-yellow{background:var(--yellow);color:var(--ink)}
.about .btn{position:absolute;left:176px;top:512px;width:116px;height:34px;line-height:34px}
.ph-window-small{left:612px;top:192px;width:200px;height:222px;background:linear-gradient(135deg,#6d3a22,#9a5a36);border:14px solid #6a3820}
.ph-door{left:872px;top:84px;width:196px;height:470px;background:linear-gradient(120deg,#4a1c16,#6c2c24 60%,#3e1712)}

/* Products */
.products{left:0;top:1318px;width:1200px;height:617px;background:var(--grey-bg)}
.section-title{position:absolute;left:0;width:1200px;text-align:center;font-family:"Montserrat",sans-serif;font-size:21px;font-weight:400;color:var(--ink);text-transform:uppercase}
.section-title b{font-weight:800}
.title-bar{position:absolute;left:564px;width:72px;height:6px;background:var(--yellow);border-bottom:2px solid #c8c85a}
.card{position:absolute;top:202px;width:296px;height:267px;background:var(--white)}
.card .ph{position:absolute;left:16px;top:24px;width:120px;height:222px}
.card h3{position:absolute;left:162px;top:24px;font-size:25px;font-weight:400;line-height:31px;color:var(--ink)}
.card h3 b{font-weight:800;display:block}
.card p{position:absolute;left:162px;width:118px;font-size:10px;line-height:14px;color:var(--muted)}
.card .btn{position:absolute;left:162px;top:200px;width:98px;height:34px;line-height:34px;font-size:11px}
.products .dots{position:absolute;left:566px;top:542px}
.products .dots i{background:#bbb;width:9px;height:9px}
.products .dots i.on{background:#8a8a20}

/* Latest */
.latest-band{left:0;top:2160px;width:1200px;height:500px;z-index:2}
.latest-name{left:188px;top:2340px;font-family:"Montserrat",sans-serif;font-size:30px;line-height:38px;color:var(--ink);z-index:3}
.ph-window-large{left:388px;top:2176px;width:430px;height:444px;border:8px solid var(--yellow);background:linear-gradient(180deg,#7a3c20,#5a2a16);z-index:3}
.latest-text{left:856px;top:2252px;width:212px;font-size:12px;line-height:16px;color:var(--ink);z-index:3}
.btn-outline{left:857px;top:2430px;width:108px;height:32px;line-height:28px;border:2px solid var(--ink);color:var(--ink);z-index:3}
.arrow-tab{width:38px;height:50px;background:var(--ink);display:flex;align-items:center;justify-content:center;z-index:3}

/* Footer */
.site-footer{left:0;top:2560px;width:1200px;height:455px;background:var(--black);overflow:hidden;z-index:1}
.site-footer svg{position:absolute;left:0;top:0}
.foot-mark{left:162px;top:152px;width:70px;height:70px;background:var(--green)}
.foot-brand{left:296px;top:192px;font-weight:800;font-size:25px;line-height:28px;color:var(--white);text-transform:uppercase}
.foot-brand span{display:block;font-size:16px;line-height:22px}
.foot-col h4{font-family:"Montserrat",sans-serif;font-weight:700;font-size:11px;color:var(--white);margin-bottom:22px;text-transform:uppercase}
.foot-col li{list-style:none;font-size:11px;line-height:18px;color:#e6e6e6}
.foot-col .addr{padding-left:22px;position:relative}
.foot-col .addr svg,.foot-col .tel svg{position:absolute;left:0;top:3px}
.foot-col .tel{position:relative;padding-left:22px;margin-top:18px}
.social li{display:flex;align-items:center;gap:12px;margin-bottom:12px}
.social .dot{width:26px;height:26px;border-radius:50%;background:#2a6bb0;display:block}
.foot-rule{left:132px;top:352px;width:936px;height:1px;background:#444}
.copyright{left:0;top:396px;width:1200px;text-align:center;font-size:11px;color:#e6e6e6}
</style>
</head>
<body>

<header class="site-header">
  <div class="abs brand-mark"></div>
  <div class="abs brand">Halvenmoor<span>Fabrication Ltd.</span></div>
  <div class="abs call">
    <div class="call-icon"><svg width="16" height="16" viewBox="0 0 24 24"><path fill="#fff" d="M6.6 10.8a15.1 15.1 0 0 0 6.6 6.6l2.2-2.2c.3-.3.7-.4 1-.2 1.1.4 2.3.6 3.6.6.6 0 1 .4 1 1V20c0 .6-.4 1-1 1A17 17 0 0 1 3 4c0-.6.4-1 1-1h3.5c.6 0 1 .4 1 1 0 1.3.2 2.5.6 3.6.1.3 0 .7-.2 1z"/></svg></div>
    <div><small>CALL US NOW</small><strong>+44 (0)1632 960 418</strong></div>
  </div>
  <div class="abs header-rule"></div>
  <nav class="abs nav">
    <a class="active" href="#">Home</a><a href="#">Products</a><a href="#">Accessories</a><a href="#">Delivery &amp; Lead Times</a><a href="#">Downloads</a><a href="#">Contact</a>
  </nav>
</header>

<section class="abs hero" role="img" aria-label="Close-up photo of a wooden steel security door with handle and locking bolts">
  <h1>STEEL<em>SECURITY</em>DOORS</h1>
  <a class="btn btn-teal" href="#">Read More</a>
  <div class="dots"><i></i><i></i><i class="on"></i><i></i><i></i></div>
</section>

<section class="abs about">
  <svg width="1200" height="635" viewBox="0 0 1200 635" aria-hidden="true">
    <polygon fill="#1c1c1c" points="0,0 110,0 -80,635 -190,635"/>
    <polygon fill="#1c1c1c" points="250,0 470,0 280,635 60,635"/>
    <polygon fill="#1c1c1c" points="700,0 820,0 630,635 510,635"/>
    <polygon fill="#1c1c1c" points="1010,0 1200,0 1200,100 1040,635 820,635"/>
  </svg>
  <h2>WHAT WE DO</h2>
  <div class="rule"></div>
  <div class="about-text">
    <p>Halvenmoor security doors combine a high level of security with exceptional value.</p>
    <p>Our superior quality and proven reliability has made us the first choice for a wide range of companies no matter what their requirement or application.</p>
    <p>All of our products are designed and manufactured to the highest specification, combine this with a rigorous quality control system and an extensive after-sales service and it is easy to see why we are seen as industry leaders.</p>
    <p>We place particular emphasis on continuous development and twelve years experience ensures that we are always ahead of the competition and that we can react quickly to customer's requirements.</p>
    <p>Each and every Halvenmoor product is subject to our fifty point quality control process before it is dispatched.</p>
  </div>
  <a class="btn btn-yellow" href="#">Read More</a>
  <div class="abs ph-window-small" role="img" aria-label="Brown double casement window unit"></div>
  <div class="abs ph-door" role="img" aria-label="Open dark red steel security door"></div>
</section>

<section class="abs products">
  <h2 class="section-title" style="top:78px">Our <b>Products</b></h2>
  <div class="title-bar" style="top:117px"></div>

  <article class="card" style="left:132px">
    <div class="ph" role="img" aria-label="Grey steel fire exit door with push bar" style="background:linear-gradient(180deg,#c9c9c9,#9d9d9d)"></div>
    <h3>Fire<b>Exit</b>Doors</h3>
    <p style="top:132px">Halvenmoor steel fire exit doors are designed.</p>
    <a class="btn btn-yellow" href="#">Read More</a>
  </article>
  <article class="card" style="left:450px">
    <div class="ph" role="img" aria-label="Red steel personnel door with lock" style="left:22px;width:102px;top:34px;height:200px;background:linear-gradient(180deg,#d42020,#8e1010)"></div>
    <h3>Personnel<b>Doors</b></h3>
    <p style="top:98px">Halvenmoor steel security doors are the ideal solution for a wide</p>
    <a class="btn btn-yellow" href="#">Read More</a>
  </article>
  <article class="card" style="left:772px">
    <div class="ph" role="img" aria-label="Black anti-vandal steel window shutter" style="left:24px;top:46px;width:118px;height:160px;background:linear-gradient(135deg,#2a2a2a,#0e0e0e)"></div>
    <h3 style="left:162px">Anti-<br>Vandal<b>shutters</b></h3>
    <p style="top:132px">Halvenmoor anti-vandal steel window shutters</p>
    <a class="btn btn-yellow" href="#">Read More</a>
  </article>

  <div class="dots"><i></i><i></i><i class="on"></i><i></i><i></i></div>
</section>

<h2 class="section-title" style="top:2030px">Latest <b>Products</b></h2>
<div class="title-bar" style="top:2078px"></div>

<footer class="abs site-footer">
  <svg width="1200" height="455" viewBox="0 0 1200 455" aria-hidden="true">
    <polygon fill="#2c2f1f" points="90,0 260,0 130,455 -40,455"/>
    <polygon fill="#2c2f1f" points="520,0 740,0 610,455 390,455"/>
    <polygon fill="#2c2f1f" points="980,0 1130,0 1000,455 850,455"/>
  </svg>
  <div class="abs foot-mark"></div>
  <div class="abs foot-brand">Halvenmoor<span>Fabrication Ltd.</span></div>

  <div class="abs foot-col" style="left:546px;top:138px">
    <h4>Contact Us</h4>
    <ul>
      <li class="addr"><svg width="10" height="14" viewBox="0 0 10 14"><path fill="#fff" d="M5 0a5 5 0 0 0-5 5c0 4 5 9 5 9s5-5 5-9a5 5 0 0 0-5-5zm0 7a2 2 0 1 1 0-4 2 2 0 0 1 0 4z"/></svg>Brackley Rise<br>Ferrow Lane<br>Ostwick<br>Hull<br>UK<br>HU9 4QT</li>
      <li class="tel"><svg width="12" height="12" viewBox="0 0 24 24"><path fill="#fff" d="M6.6 10.8a15.1 15.1 0 0 0 6.6 6.6l2.2-2.2c.3-.3.7-.4 1-.2 1.1.4 2.3.6 3.6.6.6 0 1 .4 1 1V20c0 .6-.4 1-1 1A17 17 0 0 1 3 4c0-.6.4-1 1-1h3.5c.6 0 1 .4 1 1 0 1.3.2 2.5.6 3.6.1.3 0 .7-.2 1z"/></svg>+44 (0) 1632 960418</li>
    </ul>
  </div>
  <div class="abs foot-col" style="left:803px;top:138px">
    <h4>Menu</h4>
    <ul><li>Home</li><li>Products</li><li>Accessories</li><li>Delivery &amp; lead times</li><li>Downloads</li><li>Contact</li></ul>
  </div>
  <div class="abs foot-col social" style="left:1007px;top:138px">
    <h4>Connect With Us</h4>
    <ul>
      <li><span class="dot"></span>Friendpage</li>
      <li><span class="dot" style="background:#2a9ad6"></span>Chirpline</li>
      <li><span class="dot" style="background:#1d3f7a"></span>Workweave</li>
    </ul>
  </div>
  <div class="abs foot-rule"></div>
  <p class="abs copyright">Copyrights @ 2018 All Rights Reserved</p>
</footer>

<svg class="abs latest-band" width="1200" height="500" viewBox="0 0 1200 500" aria-hidden="true">
  <polygon fill="#f2f20a" points="0,82 1200,0 1200,400 0,488"/>
</svg>
<div class="abs latest-name">Security<br>Window</div>
<div class="abs ph-window-large" role="img" aria-label="Brown wooden double casement security window"></div>
<p class="abs latest-text">Sed ut perspiciatis unde omnis iste natus error sit voluptatem accusa ntium doloremque lauda ntium, totam rem aperiam, eaque ipsa quae ab illo inventore veritatis et quasi architecto beatae vitae dicta sunt explicabo. Nemo enim ipsam volu ptatem quia voluptas sit as pernatur</p>
<a class="abs btn btn-outline" href="#">Read More</a>
<div class="abs arrow-tab" style="left:0;top:2414px"><svg width="12" height="16" viewBox="0 0 12 16"><path d="M10 2 3 8l7 6" stroke="#fff" stroke-width="3" fill="none"/></svg></div>
<div class="abs arrow-tab" style="left:1162px;top:2330px"><svg width="12" height="16" viewBox="0 0 12 16"><path d="m2 2 7 6-7 6" stroke="#fff" stroke-width="3" fill="none"/></svg></div>

</body>
</html>
```